External Window Signage Design – Antiaging Center

I would like to dress our shop windows in order to promote our activities in medical aesthetics, meso-aesthetics, anti-ageing care and classical beauty. In fact, our 350 m² center is located on the first floor of a building where there is a lot of traffic, as well as a bus stop and metro station. And right in front of a twenty-floor building of the Northern Assembly.
We want to communicate our activities to our customers with photos and text in a storefront window. So that they can what we do and visit our website www.lumivora.be (our site is in French) as well as our social networks, like instragram, facebook,…
We'd like a window signage : Elegant, Modern, New, Pure, Clean
We are located on the corners of a building, where we have 8 windows on one side and 10 windows on the other, the dimensions are :
Windows
• Height: 125 cm
• Width: 130 cm
Small windows
• Height: 134 cm
• Width: 40 cm
I would say let your imagination go free. I will have other projects for the winner.
Don't hesitate to ask me if you need other formats of the logo or color, like white.
Updates

https://www.brieflyhub.com/design/58204719, I'D LIKE TO HAVE A PROJECT LIKE THIS IF POSSIBLE WITH THE LITTLE WINDOW UNDERNEATH AS WELL.

Target Market(s)

People who want to take care of their external appearance, look beautiful and good looking, womens/girls - mens/boys

Requirements
Must have
• Face and silhouette of a woman. Elegant
Serious, Modern, Professional, Feminine,Upmarket
Nice to have
• To put the different treatments that we propose,
Should not have
• We absolutely don't want a classic beauty center signage, which is reviewed many times

```html
<!DOCTYPE html>
<html lang="fr">
<head>
<meta charset="utf-8">
<title>Lumivora – vitrines</title>
<link href="https://fonts.googleapis.com/css2?family=Montserrat:wght@500;600;700&family=Oswald:wght@400&display=swap" rel="stylesheet">
<style>
  :root {
    --gold: #b59d5e;
    --charcoal: #3b3b3b;
    --ink: #2f2f2f;
    --stage: #e2e2e2;
    --white: #ffffff;
  }
  * { margin: 0; padding: 0; box-sizing: border-box; }
  html, body { width: 1200px; height: 400px; overflow: hidden; }
  body {
    background: var(--stage);
    font-family: "Montserrat", Arial, sans-serif;
    position: relative;
  }
  .window {
    position: absolute;
    top: 119px;
    width: 127px;
    height: 121px;
    overflow: hidden;
    box-shadow: 0 4px 12px rgba(0,0,0,.25);
  }
  .window--text { background: linear-gradient(160deg, var(--white) 0%, #ececec 60%, #f5f5f5 100%); }
  .photo { position: absolute; inset: 0; }
  .photo--curls { background: linear-gradient(135deg, #9aa19c 0%, #7d6a5e 45%, #8f958f 100%); }
  .photo--sunlit { background: linear-gradient(135deg, #5a3a24 0%, #b07a4f 50%, #3a261a 100%); }
  .photo--peach { background: radial-gradient(circle at 50% 40%, #d9a98a 0%, #f3c6a8 55%, #f6c9aa 100%); }
  .photo--silhouette { background: linear-gradient(135deg, #c9c6d2 0%, #e8d8cc 50%, #b9b6c4 100%); }
  .wave { position: absolute; left: 0; bottom: 0; width: 127px; height: 34px; }
  .brand { position: absolute; left: 12px; top: 9px; display: flex; align-items: center; gap: 4px; }
  .brand__dot { width: 13px; height: 13px; border-radius: 50%; background: var(--gold); flex: none; }
  .brand__name { font-size: 17px; font-weight: 700; color: var(--ink); letter-spacing: -0.5px; line-height: 1; }
  .brand__tag { position: absolute; left: 47px; top: 27px; font-size: 5px; font-weight: 500; color: var(--ink); }
  .services { position: absolute; left: 11px; list-style: none; }
  .services li {
    font-size: 6.3px; font-weight: 600; color: var(--ink);
    line-height: 9.6px; white-space: nowrap; display: flex; align-items: center; gap: 4px;
  }
  .services li::before {
    content: ""; width: 4px; height: 4px; border-radius: 50%;
    border: 1px solid var(--gold); flex: none;
  }
  .sill {
    position: absolute;
    top: 243px;
    width: 130px;
    height: 38px;
    background: var(--gold);
    color: var(--white);
    display: flex; flex-direction: column; align-items: center; justify-content: center;
    text-align: center;
    box-shadow: 0 4px 10px rgba(0,0,0,.25);
    overflow: hidden;
  }
  .sill__curve { position: absolute; left: 0; top: 0; width: 130px; height: 14px; }
  .sill__body { position: relative; z-index: 1; white-space: nowrap; }
  .sill--contact { font-size: 9px; font-weight: 500; line-height: 13.5px; letter-spacing: .3px; }
  .sill--web { font-size: 8.5px; font-weight: 500; letter-spacing: 1.2px; }
  .sill--address { font-family: "Oswald", "Arial Narrow", sans-serif; font-size: 7.3px; line-height: 10px; }
  .sill--welcome { font-family: "Oswald", "Arial Narrow", sans-serif; font-size: 8.4px; line-height: 12px; text-align: left; align-items: flex-start; padding-left: 13px; }
  .socials { display: flex; gap: 5px; margin-top: 12px; }
  .socials span { width: 12px; height: 12px; border-radius: 50%; border: 1px solid var(--white); }
  .icon { display: inline-block; vertical-align: -1px; margin-right: 3px; }
</style>
</head>
<body>

<div class="window" style="left:53px">
  <div class="photo photo--curls" role="img" aria-label="Portrait of a woman with long curly hair on a grey background"></div>
  <svg class="wave" viewBox="0 0 127 34"><path d="M0 18 Q55 2 127 0 L127 34 L0 34Z" fill="var(--charcoal)"/><path d="M0 26 Q60 10 127 8" stroke="#fff" stroke-width="1.4" fill="none"/><path d="M0 28 Q60 12 127 10 L127 34 L0 34Z" fill="var(--gold)"/></svg>
</div>
<div class="sill sill--contact" style="left:52px">
  <div class="sill__body">
    <div><svg class="icon" width="7" height="5" viewBox="0 0 7 5"><rect x=".4" y=".4" width="6.2" height="4.2" fill="none" stroke="#fff" stroke-width=".7"/><path d="M.4 .4 L3.5 3 L6.6 .4" fill="none" stroke="#fff" stroke-width=".7"/></svg>info@lumivora.be</div>
    <div><svg class="icon" width="7" height="7" viewBox="0 0 7 7"><circle cx="3.5" cy="3.5" r="3" fill="none" stroke="#fff" stroke-width=".7"/><path d="M2.3 2 Q2.3 4.7 5 4.8" stroke="#fff" stroke-width=".9" fill="none"/></svg>+32 (0)2 555 01 47</div>
  </div>
</div>

<div class="window window--text" style="left:190.5px">
  <div class="brand"><span class="brand__dot"></span><span class="brand__name">Lumivora</span></div>
  <div class="brand__tag">Antiaging Center</div>
  <ul class="services" style="top:39px">
    <li>ANTIAGING</li><li>TRAITEMENT DE PEAU</li><li>AMINCISSEMENT &amp; CELLULITE</li>
    <li>TRAITEMENT LASER</li><li>BEAUTÉ ESTHÉTIQUE</li><li>TRAITEMENT DIVERS</li>
  </ul>
  <svg class="wave" viewBox="0 0 127 34"><path d="M0 4 Q70 18 127 30 L127 34 L0 34Z" fill="var(--charcoal)"/><path d="M0 11 Q70 22 127 33" stroke="#fff" stroke-width="1.4" fill="none"/><path d="M0 12 Q70 24 127 34 L0 34Z" fill="var(--gold)"/></svg>
</div>
<div class="sill sill--web" style="left:189.5px">
  <svg class="sill__curve" viewBox="0 0 130 14"><path d="M0 0 L130 0 L130 6 Q100 2 70 0Z" fill="var(--charcoal)"/><path d="M72 0 Q104 2 130 7" stroke="#fff" stroke-width="1" fill="none"/></svg>
  <div class="sill__body"><svg class="icon" width="7" height="7" viewBox="0 0 7 7"><circle cx="3.5" cy="3.5" r="3" fill="none" stroke="#fff" stroke-width=".7"/><ellipse cx="3.5" cy="3.5" rx="1.3" ry="3" fill="none" stroke="#fff" stroke-width=".6"/><path d="M.5 3.5 H6.5" stroke="#fff" stroke-width=".6"/></svg>www.lumivora.be</div>
</div>

<div class="window" style="left:328px">
  <div class="photo photo--sunlit" role="img" aria-label="Sunlit woman with dark hair looking down"></div>
</div>
<div class="sill" style="left:327px">
  <svg class="sill__curve" viewBox="0 0 130 14"><rect width="130" height="14" fill="#4a3020"/><path d="M0 4 Q60 14 130 4 L130 14 L0 14Z" fill="var(--charcoal)"/><path d="M0 9 Q65 17 130 7" stroke="#fff" stroke-width="1" fill="none"/><path d="M0 10 Q65 18 130 8 L130 14 L0 14Z" fill="var(--gold)"/></svg>
  <div class="sill__body socials"><span></span><span></span><span></span><span></span></div>
</div>

<div class="window window--text" style="left:465.5px">
  <div class="brand"><span class="brand__dot"></span><span class="brand__name">Lumivora</span></div>
  <div class="brand__tag">Antiaging Center</div>
  <ul class="services" style="top:43px">
    <li>SKIN RÉJUVÉNATION</li><li>LIFTING VISAGE</li><li>RADIOFRÉQUENCE</li>
    <li>HIFU</li><li>SOIN HYDRATANT</li><li>SOIN NOVADERM</li>
  </ul>
  <svg class="wave" viewBox="0 0 127 34"><path d="M0 34 Q70 30 127 18 L127 34Z" fill="var(--charcoal)"/></svg>
</div>
<div class="sill sill--web" style="left:464.5px">
  <svg class="sill__curve" viewBox="0 0 130 14"><rect width="130" height="14" fill="#f1cfb5"/><path d="M0 10 Q70 4 130 0 L130 14 L0 14Z" fill="var(--charcoal)"/><path d="M0 12 Q70 7 130 3" stroke="#fff" stroke-width="1" fill="none"/><path d="M0 13 Q70 8 130 4 L130 14 L0 14Z" fill="var(--gold)"/></svg>
  <div class="sill__body" style="margin-top:10px"><svg class="icon" width="7" height="7" viewBox="0 0 7 7"><circle cx="3.5" cy="3.5" r="3" fill="none" stroke="#fff" stroke-width=".7"/><ellipse cx="3.5" cy="3.5" rx="1.3" ry="3" fill="none" stroke="#fff" stroke-width=".6"/><path d="M.5 3.5 H6.5" stroke="#fff" stroke-width=".6"/></svg>www.lumivora.be</div>
</div>

<div class="window" style="left:603px">
  <div class="photo photo--peach" role="img" aria-label="Portrait of a dark-haired woman on a peach background"></div>
  <svg class="wave" viewBox="0 0 127 34"><path d="M0 14 Q60 8 127 12 L127 34 L0 34Z" fill="var(--charcoal)"/><path d="M0 23 Q60 16 127 22" stroke="#fff" stroke-width="1.4" fill="none"/><path d="M0 25 Q60 18 127 24 L127 34 L0 34Z" fill="var(--gold)"/></svg>
</div>
<div class="sill sill--address" style="left:602px">
  <div class="sill__body">Place Verdane,<br>Avenue des Lys 14, Premier étage<br>4820 Valmont</div>
</div>

<div class="window window--text" style="left:740.5px">
  <div class="brand"><span class="brand__dot"></span><span class="brand__name">Lumivora</span></div>
  <div class="brand__tag">Antiaging Center</div>
  <ul class="services" style="top:42px">
    <li>ANALYSE DE PEAU</li><li>TRAITEMENT ACNÉ</li><li>TACHE PIGMENTAIRE</li>
    <li>PEELING</li><li>SOIN HYDRATANT</li><li>TRAITEMENTS ESTHÉTIQUES</li>
  </ul>
  <svg class="wave" viewBox="0 0 127 34"><path d="M0 20 Q70 22 127 34 L0 34Z" fill="var(--charcoal)"/><path d="M0 28 Q60 27 110 34" stroke="#fff" stroke-width="1.2" fill="none"/></svg>
</div>
<div class="sill sill--welcome" style="left:739.5px">
  <svg class="sill__curve" viewBox="0 0 130 14"><path d="M0 0 L130 0 L130 6 Q100 1 60 0Z" fill="var(--charcoal)"/><path d="M62 0 Q104 2 130 7" stroke="#fff" stroke-width="1" fill="none"/></svg>
  <div class="sill__body">BIENVENUE DANS NOTRE<br>TOUT NOUVEAU CENTRE À VERDANE</div>
</div>

<div class="window" style="left:878px">
  <div class="photo photo--silhouette" role="img" aria-label="Slim woman's silhouette in white lingerie with a measuring tape"></div>
</div>
<div class="sill sill--web" style="left:877px">
  <svg class="sill__curve" viewBox="0 0 130 14"><rect width="130" height="14" fill="#d8cfd2"/><path d="M0 2 Q65 10 130 2 L130 14 L0 14Z" fill="var(--charcoal)"/><path d="M0 7 Q65 15 130 5" stroke="#fff" stroke-width="1" fill="none"/><path d="M0 8 Q65 16 130 6 L130 14 L0 14Z" fill="var(--gold)"/></svg>
  <div class="sill__body" style="margin-top:10px"><svg class="icon" width="7" height="7" viewBox="0 0 7 7"><circle cx="3.5" cy="3.5" r="3" fill="none" stroke="#fff" stroke-width=".7"/><ellipse cx="3.5" cy="3.5" rx="1.3" ry="3" fill="none" stroke="#fff" stroke-width=".6"/><path d="M.5 3.5 H6.5" stroke="#fff" stroke-width=".6"/></svg>www.lumivora.be</div>
</div>

<div class="window window--text" style="left:1015.5px">
  <div class="brand"><span class="brand__dot"></span><span class="brand__name">Lumivora</span></div>
  <div class="brand__tag">Antiaging Center</div>
  <ul class="services" style="top:38px">
    <li>ÉPILATION LASER À FROID</li><li>LIPOCAVITATION</li><li>MÉSOTHÉRAPIE</li>
    <li>LIPOLASER</li><li>ANTICELLULITE</li><li>LUMINOTHÉRAPIE</li>
  </ul>
  <svg class="wave" viewBox="0 0 127 34"><path d="M0 28 Q50 4 127 4 L127 34 L0 34Z" fill="var(--charcoal)"/><path d="M0 32 Q55 12 127 14" stroke="#fff" stroke-width="1.4" fill="none"/><path d="M0 34 Q55 14 127 16 L127 34Z" fill="var(--gold)"/></svg>
</div>
<div class="sill sill--contact" style="left:1014.5px">
  <div class="sill__body">
    <div><svg class="icon" width="7" height="5" viewBox="0 0 7 5"><rect x=".4" y=".4" width="6.2" height="4.2" fill="none" stroke="#fff" stroke-width=".7"/><path d="M.4 .4 L3.5 3 L6.6 .4" fill="none" stroke="#fff" stroke-width=".7"/></svg>info@lumivora.be</div>
    <div><svg class="icon" width="7" height="7" viewBox="0 0 7 7"><circle cx="3.5" cy="3.5" r="3" fill="none" stroke="#fff" stroke-width=".7"/><path d="M2.3 2 Q2.3 4.7 5 4.8" stroke="#fff" stroke-width=".9" fill="none"/></svg>+32 (0)2 555 01 47</div>
  </div>
</div>

</body>
</html>
```